The Lumo-Hub for Rescue Instruction + Venue Readiness Post Card

Hi! I am a new business that is Licensed Training Provider to the National Bluefield Aid. We teach private CPR/AED, First Aid and a variety of other emergency training courses to the general public! Our goal is to get into businesses of all sizes from the mom and pops store to corporate offices of Manhattan. We can do private classes in your home and no office space is to small! We even have a school assembly program that teaches "Hands Only CPR" for children. I'm looking to make a post card to hand out that can easily explain what we are doing…that might have some good visuals that catch your eye as well. I def want to use The Lumo Hub logo in it that I have attached. Im not necessarily married to any of the other images. You can check out our website www.lumohubinstruct.example for more information and you can use any of the images on there as well if you would like. I will give you free reign to find any cool photo stock image that you might think fits with what I'm trying to do. Hopefully you can help!
Updates

Also feel free to use any other photos that you might find that you think fit our cause for teaching CPR/First aid etc!! Thanks!

Thank you all for your hard work. I actually like many of these designs and really torn! I will be making some decisions in the next day or so. Thank you! Dale

Industry/Entity Type

Training

```html
<!DOCTYPE html>
<html lang="en">
<head>
<meta charset="utf-8">
<title>The Lumo Hub – Post Card</title>
<link rel="stylesheet" href="https://fonts.googleapis.com/css2?family=Roboto:wght@300;400;700;900&family=Roboto+Condensed:wght@700&display=swap">
<style>
  :root {
    --red: #e2231a;
    --black: #111111;
    --white: #ffffff;
    --page: #eeeae4;
    --photo-light: #e9e3d8;
    --photo-mid: #c9bda9;
    --photo-dark: #5a5048;
    --icon-grey: #3a3a3a;
  }
  * { margin: 0; padding: 0; box-sizing: border-box; }
  html, body { width: 1200px; height: 554px; overflow: hidden; }
  body {
    position: relative;
    background: var(--page);
    font-family: "Roboto", Arial, sans-serif;
  }

  /* Front card */
  .card-front {
    position: absolute; left: 31px; top: 29px;
    width: 535px; height: 417px;
    background: var(--white);
    overflow: hidden;
    box-shadow: 0 2px 6px rgba(0,0,0,.25);
  }
  .front-header {
    position: absolute; left: 0; top: 0; width: 100%; height: 106px;
    background: var(--black);
  }
  .brand-name {
    position: absolute; left: 20px; top: 12px;
    font-weight: 300; font-size: 54px; letter-spacing: 1px;
    color: var(--white); line-height: 1;
  }
  .brand-tagline {
    position: absolute; right: 18px; top: 84px;
    font-family: "Roboto Condensed", Arial, sans-serif;
    font-weight: 700; font-size: 13px; letter-spacing: .3px;
    color: var(--red); text-transform: uppercase;
  }
  .front-photo {
    position: absolute; left: 0; top: 106px; width: 100%; height: 265px;
    background: linear-gradient(180deg, var(--photo-light) 0%, var(--photo-mid) 55%, var(--photo-dark) 100%);
  }
  .front-headline {
    position: absolute; left: 256px; top: 286px;
    font-weight: 700; font-size: 29px; color: var(--black); line-height: 1;
  }
  .front-subline {
    position: absolute; left: 362px; top: 324px;
    font-weight: 700; font-size: 27px; color: var(--red); line-height: 1;
  }
  .front-footer {
    position: absolute; left: 0; top: 371px; width: 100%; height: 46px;
    background: var(--black);
  }
  .front-web {
    position: absolute; left: 14px; top: 13px;
    font-weight: 700; font-size: 17px; color: var(--white);
  }
  .front-phone {
    position: absolute; right: 0; top: -6px; width: 189px; height: 52px;
    background: var(--red); color: var(--white);
    font-weight: 700; font-size: 20px;
    display: flex; align-items: center; justify-content: center;
  }

  /* Back card */
  .card-back {
    position: absolute; left: 614px; top: 45px;
    width: 557px; height: 458px;
    background: var(--white);
    overflow: hidden;
    box-shadow: 0 2px 6px rgba(0,0,0,.25);
  }
  .back-heading {
    position: absolute; left: 50px; top: 66px;
    font-weight: 900; font-size: 36px; line-height: 1.02;
    color: var(--red); text-align: center; letter-spacing: -.5px;
  }
  .back-heading .answer {
    display: block; color: var(--black); font-weight: 700; font-size: 28px; margin-top: 4px;
  }
  .contact-box {
    position: absolute; left: 311px; top: 108px; width: 246px; height: 90px;
    background: var(--red); color: var(--white);
    padding: 16px 0 0 12px;
    font-weight: 700; font-size: 15px; line-height: 1.3;
  }
  .hazard-icons {
    position: absolute; left: 12px; top: 190px; width: 296px; height: 54px;
    background: linear-gradient(90deg, var(--icon-grey), #5c5c5c, var(--icon-grey));
    opacity: .85;
  }
  .info-panel {
    position: absolute; top: 252px; height: 165px;
    background: var(--black); border-radius: 8px;
    padding: 7px 8px 0 8px;
    color: var(--white);
  }
  .info-panel.services { left: 12px; width: 292px; }
  .info-panel.clients { left: 319px; width: 186px; }
  .panel-title {
    font-family: "Roboto Condensed", Arial, sans-serif;
    font-weight: 700; font-size: 10.5px; color: var(--red);
    text-transform: uppercase; margin-bottom: 4px;
  }
  .panel-list { list-style: none; }
  .panel-list li {
    font-family: "Roboto Condensed", Arial, sans-serif;
    font-weight: 700; font-size: 9.3px; line-height: 10.3px;
  }
  .panel-list li::before { content: "• "; }
  .back-footer {
    position: absolute; left: 12px; top: 423px; width: 319px; height: 35px;
    background: var(--red); color: var(--white);
    font-family: "Roboto Condensed", Arial, sans-serif;
    font-weight: 700; font-size: 17px;
    display: flex; align-items: center; padding-left: 12px;
  }
  .back-brand {
    position: absolute; left: 331px; top: 423px; width: 226px; height: 35px;
    background: var(--black);
    padding: 3px 0 0 12px;
  }
  .back-brand .brand-name-small {
    font-weight: 300; font-size: 20px; color: var(--white); line-height: 1;
  }
  .back-brand .brand-tagline-small {
    font-family: "Roboto Condensed", Arial, sans-serif;
    font-weight: 700; font-size: 6.5px; color: var(--red);
    text-transform: uppercase; margin-top: 2px;
  }
</style>
</head>
<body>

<section class="card-front">
  <header class="front-header">
    <div class="brand-name">THE LUMO HUB</div>
    <div class="brand-tagline">Rescue Instruction + Venue Readiness</div>
  </header>
  <div class="front-photo" role="img" aria-label="Photo of hands performing CPR chest compressions on a person lying down"></div>
  <div class="front-headline">Get CPR trained.</div>
  <div class="front-subline">Save a LIFE</div>
  <footer class="front-footer">
    <div class="front-web">www.lumohubinstruct.example</div>
    <div class="front-phone">555 010 4417</div>
  </footer>
</section>

<section class="card-back">
  <h1 class="back-heading">Ready for an<br>Emergency?<span class="answer">You can be.</span></h1>
  <div class="contact-box">
    Contact: Dale Brenner<br>
    lumohub911@example.com<br>
    555 010 4417
  </div>
  <div class="hazard-icons" role="img" aria-label="Row of disaster illustrations: landslide, volcano, earthquake, tsunami wave and flood"></div>

  <div class="info-panel services">
    <div class="panel-title">Services we provide:</div>
    <ul class="panel-list">
      <li>National Certification In Variety Of CPR/AED/First Aid/O2 Courses</li>
      <li>National Bluefield Aid Lifeguard Training</li>
      <li>Standby Ambulances Paramedics / EMTS</li>
      <li>Lifeguards For All Events</li>
      <li>Rescue Board Rentals</li>
      <li>Marine Safety Coordination</li>
      <li>Certified Rescue Divers</li>
      <li>Communications Rentals</li>
      <li>Customized Emergency Action Plans</li>
      <li>First Aid Kits/supplies</li>
      <li>Athletic Trainers</li>
      <li>Safety Walk Throughs</li>
      <li>Fireguards</li>
    </ul>
  </div>

  <div class="info-panel clients">
    <div class="panel-title">Organizations we work with:</div>
    <ul class="panel-list">
      <li>Police / Fire / EMS Departments</li>
      <li>Race Directors / Event Coordinators</li>
      <li>Gyms/fitness Centers</li>
      <li>Doctors Office</li>
      <li>Public And Private Schools</li>
      <li>Colleges / Universities</li>
      <li>Corporations</li>
      <li>Private Owned Businesses</li>
      <li>Restaurants</li>
      <li>Beach Clubs</li>
      <li>Sleep-away/ Day Camps</li>
    </ul>
  </div>

  <div class="back-footer">HEALTH IS YOUR GREATEST WEALTH</div>
  <div class="back-brand">
    <div class="brand-name-small">THE LUMO HUB</div>
    <div class="brand-tagline-small">Rescue Instruction + Venue Readiness</div>
  </div>
</section>

</body>
</html>
```